plumfable business card

need to upgrade current business card for an online retailer of handmade arts and crafts, please visit plumfable.com.au

need to be artistic professional look

sample layout, contents, logo, are in the attached files

need for 4 people, details for other 2 people to be provided later

```html
<!DOCTYPE html>
<html lang="en">
<head>
<meta charset="utf-8">
<title>PlumFable Business Card</title>
<link href="https://fonts.googleapis.com/css2?family=PT+Sans:wght@400;700&family=PT+Sans+Narrow:wght@400;700&family=PT+Serif:ital,wght@0,700;1,700&display=swap" rel="stylesheet">
<style>
  :root {
    --page: #e8e5e0;
    --card: #ffffff;
    --card-shade: #ececec;
    --red: #d9211d;
    --red-dark: #b81713;
    --black: #1b1b1b;
    --ink: #2a2a2a;
    --muted: #555555;
    --rule: #3a3a3a;
  }
  * { margin: 0; padding: 0; box-sizing: border-box; }
  html, body { width: 1200px; height: 1024px; overflow: hidden; }
  body {
    background: var(--page);
    font-family: "PT Sans", Arial, sans-serif;
    color: var(--ink);
    position: relative;
  }
  .card {
    position: absolute;
    left: 220px;
    width: 760px;
    height: 434px;
    background: linear-gradient(180deg, var(--card) 0%, var(--card-shade) 100%);
    overflow: hidden;
    box-shadow: 0 3px 10px rgba(0,0,0,0.12);
  }
  .card--front { top: 60px; }
  .card--back { top: 554px; }

  .brand-name {
    font-family: "PT Serif", Georgia, serif;
    font-weight: 700;
    color: var(--ink);
    letter-spacing: -0.5px;
  }
  .tagline {
    font-family: "PT Sans", Arial, sans-serif;
    font-size: 22px;
    color: var(--muted);
    letter-spacing: 1px;
  }

  /* Front */
  .front-brand { position: absolute; left: 50px; top: 56px; }
  .front-brand .brand-name { font-size: 64px; line-height: 1; }
  .front-brand .tagline { margin-top: 8px; margin-left: 4px; }
  .front-rule {
    position: absolute; left: 50px; top: 196px; width: 430px;
    height: 1px; background: var(--rule);
  }
  .person { position: absolute; right: 50px; top: 170px; text-align: left; }
  .person__name {
    font-family: "PT Sans Narrow", Arial, sans-serif;
    font-size: 28px; color: var(--red); font-weight: 400;
    line-height: 1;
  }
  .person__role {
    font-family: "PT Sans Narrow", Arial, sans-serif;
    font-size: 17px; color: var(--ink); margin-top: 6px;
  }
  .contacts { position: absolute; left: 50px; top: 226px; list-style: none; }
  .contacts li {
    display: flex; align-items: center; gap: 14px;
    font-size: 21px; color: var(--ink); height: 38px;
  }
  .contacts svg { width: 24px; height: 24px; flex: none; }
  .front-band { position: absolute; left: 0; bottom: 0; width: 760px; height: 80px; }

  /* Back */
  .back-brand { position: absolute; left: 0; right: 0; top: 34px; text-align: center; }
  .back-brand .brand-name { font-size: 56px; line-height: 1; }
  .back-brand .tagline { margin-top: 6px; font-size: 20px; }
  .band-black {
    position: absolute; left: 0; top: 152px; width: 100%; height: 44px;
    background: var(--black);
    display: flex; align-items: center; justify-content: center;
    font-family: "PT Serif", Georgia, serif; font-style: italic; font-weight: 700;
    color: var(--red); font-size: 20px;
  }
  .band-red {
    position: absolute; left: 0; top: 196px; width: 100%; height: 44px;
    background: var(--red);
    display: flex; align-items: center; justify-content: center;
    font-family: "PT Sans Narrow", Arial, sans-serif; font-weight: 700;
    color: #fff; font-size: 22px; letter-spacing: 0.5px;
  }
  .products {
    position: absolute; left: 90px; right: 90px; top: 258px;
    display: flex; justify-content: space-between;
  }
  .products ul { list-style: none; }
  .products li {
    font-family: "PT Sans Narrow", Arial, sans-serif;
    font-size: 19px; color: var(--ink); line-height: 27px;
    padding-left: 18px; position: relative;
  }
  .products li::before {
    content: ""; position: absolute; left: 0; top: 10px;
    width: 7px; height: 7px; border-radius: 50%; background: var(--red);
  }
  .mission {
    position: absolute; left: 0; right: 0; top: 330px; text-align: center;
    font-family: "PT Sans Narrow", Arial, sans-serif; font-style: italic; font-weight: 700;
    color: var(--red); font-size: 22px;
  }
  .back-edge { position: absolute; left: 0; bottom: 0; width: 760px; height: 40px; }
</style>
</head>
<body>

<section class="card card--front" aria-label="Card front">
  <div class="front-brand">
    <div class="brand-name">PlumFable</div>
    <div class="tagline">stories made by hand</div>
  </div>
  <div class="front-rule"></div>

  <div class="person">
    <div class="person__name">Kiran Lama</div>
    <div class="person__role">Director, PlumFable Australia</div>
  </div>

  <ul class="contacts">
    <li>
      <svg viewBox="0 0 24 24" aria-hidden="true"><circle cx="12" cy="12" r="12" fill="var(--red)"/><path d="M8 6.5h2.2l1 3-1.4 1.1a7 7 0 0 0 3.6 3.6l1.1-1.4 3 1v2.2c0 .6-.5 1-1 1A11 11 0 0 1 7 7.5c0-.5.4-1 1-1z" fill="#fff"/></svg>
      <span>+61 400 555 019</span>
    </li>
    <li>
      <svg viewBox="0 0 24 24" aria-hidden="true"><circle cx="12" cy="12" r="12" fill="var(--red)"/><rect x="6" y="8" width="12" height="8.5" rx="1" fill="#fff"/><path d="M6.5 8.5 12 13l5.5-4.5" fill="none" stroke="var(--red)" stroke-width="1.3"/></svg>
      <span>kiran@plumfable.com.au</span>
    </li>
    <li>
      <svg viewBox="0 0 24 24" aria-hidden="true"><circle cx="12" cy="12" r="12" fill="var(--red)"/><g fill="none" stroke="#fff" stroke-width="1.3"><circle cx="12" cy="12" r="6"/><ellipse cx="12" cy="12" rx="2.6" ry="6"/><path d="M6 12h12"/></g></svg>
      <span>www.plumfable.com.au</span>
    </li>
  </ul>

  <svg class="front-band" viewBox="0 0 760 80" preserveAspectRatio="none" aria-hidden="true">
    <polygon points="0,30 620,30 590,80 0,80" fill="var(--red)"/>
    <polygon points="620,30 760,30 760,80 590,80" fill="var(--black)"/>
    <polygon points="620,30 640,0 760,0 760,30" fill="var(--black)"/>
    <rect x="0" y="30" width="620" height="4" fill="var(--red-dark)"/>
  </svg>
</section>

<section class="card card--back" aria-label="Card back">
  <div class="back-brand">
    <div class="brand-name">PlumFable</div>
    <div class="tagline">stories made by hand</div>
  </div>

  <div class="band-black">Visit us for exotic hand-made arts &amp; crafts around the globe</div>
  <div class="band-red">CASHMERE FASHION ITEMS FROM NEPAL</div>

  <div class="products">
    <ul>
      <li>Lokta / Rice Paper Crafts</li>
      <li>Allo / Cotton / Woollen Items</li>
    </ul>
    <ul>
      <li>Thai Traditional Paintings</li>
      <li>Nepali / Tibetan Thangkas</li>
    </ul>
  </div>

  <div class="mission">Encourage eco-friendly, sustainable and traditional arts practice.</div>

  <svg class="back-edge" viewBox="0 0 760 40" preserveAspectRatio="none" aria-hidden="true">
    <polygon points="0,8 560,8 540,40 0,40" fill="var(--black)"/>
    <polygon points="560,8 760,8 760,40 540,40" fill="var(--red)"/>
  </svg>
</section>

</body>
</html>
```